Banner Pop Up Opt In Form REDESIGNS - SLEEK BLACK LOOK

Please redesign banners attached.

I am looking for a very sleek look....I do not like this collage of images on these current designs. Please keep all content same but use images that pop.

I have an acccount at www.pixmorrow-example.com or you can use your own images.

I like black background for somereason because it looks very sleek....but these designs should pop , build trust and credibility and have easy opt in form....SLEEK AND MODERN LOOK is what im looking for....

Target Market(s)

Consumers on websites

Requirements
Must have
• Please redesign banners attached.

Nice to have

Should not have

```html
<!DOCTYPE html>
<html lang="en">
<head>
<meta charset="UTF-8">
<title>Newsletter Opt-In – Smart Fitness Watch</title>
<link rel="stylesheet" href="https://fonts.googleapis.com/css2?family=Montserrat:wght@400;800&family=Poppins:wght@300;400&display=swap">
<style>
  :root {
    --ink: #000000;
    --orange: #f7a024;
    --white: #ffffff;
    --field-text: #6f6f6f;
    --photo-light: #d9dfe3;
    --photo-mid: #a9b3ba;
    --photo-dark: #4a4f55;
    --product-dark: #2a2a2a;
    --product-mid: #3d3d3d;
  }
  * { margin: 0; padding: 0; box-sizing: border-box; }
  html, body { width: 1200px; height: 1200px; overflow: hidden; background: var(--white); }
  .banner {
    position: relative;
    width: 1200px;
    height: 1200px;
    background: var(--ink);
    overflow: hidden;
    font-family: "Montserrat", Arial, sans-serif;
  }
  .backdrop { position: absolute; inset: 0; width: 1200px; height: 1200px; }
  .headline {
    position: absolute;
    left: 62px;
    top: 82px;
    font-weight: 800;
    font-size: 70px;
    line-height: 84px;
    color: var(--white);
    letter-spacing: -0.5px;
  }
  .headline .accent { color: var(--orange); display: block; }
  .subhead {
    position: absolute;
    left: 62px;
    top: 262px;
    font-weight: 400;
    font-size: 24px;
    line-height: 33px;
    color: var(--white);
    text-transform: uppercase;
  }
  .product-shot {
    position: absolute;
    left: 62px;
    top: 365px;
    width: 256px;
    height: 312px;
    border-radius: 40px;
    background: radial-gradient(ellipse at 55% 45%, var(--product-mid), var(--product-dark) 60%, var(--ink) 100%);
  }
  .product-title {
    position: absolute;
    left: 352px;
    top: 392px;
    font-weight: 800;
    font-size: 66px;
    line-height: 82px;
    color: var(--white);
  }
  .product-title .accent { color: var(--orange); }
  .optin-form {
    position: absolute;
    left: 50px;
    top: 765px;
    width: 438px;
    font-family: "Poppins", Arial, sans-serif;
  }
  .field {
    display: block;
    width: 438px;
    height: 60px;
    margin-bottom: 15px;
    border: none;
    border-radius: 30px;
    background: var(--white);
    color: var(--field-text);
    font-family: inherit;
    font-weight: 300;
    font-size: 21px;
    text-align: center;
    line-height: 60px;
  }
  .submit-btn {
    display: block;
    width: 158px;
    height: 44px;
    margin: 5px auto 0;
    border: none;
    border-radius: 16px;
    background: var(--orange);
    color: var(--white);
    font-family: inherit;
    font-weight: 300;
    font-size: 28px;
    line-height: 44px;
    text-align: center;
  }
  .fine-print {
    position: absolute;
    left: 75px;
    top: 1124px;
    font-family: "Poppins", Arial, sans-serif;
    font-size: 14px;
    line-height: 17px;
    color: var(--white);
  }
</style>
</head>
<body>
<main class="banner">
  <svg class="backdrop" viewBox="0 0 1200 1200" aria-hidden="false">
    <defs>
      <linearGradient id="gymPhotoTone" x1="0" y1="0" x2="0" y2="1">
        <stop offset="0" stop-color="var(--photo-light)"/>
        <stop offset="0.45" stop-color="var(--photo-mid)"/>
        <stop offset="1" stop-color="var(--photo-dark)"/>
      </linearGradient>
    </defs>
    <path class="swoosh" fill="var(--orange)"
      d="M558 0 C690 150 735 320 712 440 C685 580 570 700 540 880 C520 1000 495 1100 490 1200 L1200 1200 L1200 0 Z"/>
    <path class="gym-photo" role="img" aria-label="Photo of people training on exercise bikes in a bright gym"
      fill="url(#gymPhotoTone)"
      d="M675 0 C790 150 790 320 748 420 C700 540 580 700 565 860 C555 1000 600 1120 690 1200 L1200 1200 L1200 0 Z"/>
  </svg>

  <h1 class="headline">WANT A<span class="accent">GREAT OFFER?</span></h1>
  <p class="subhead">Subscribe to our newsletter and<br>recieve complementary</p>

  <div class="product-shot" role="img" aria-label="Photo of a black smart fitness watch showing a step count"></div>
  <h2 class="product-title">SMART<br>FITNESS<br><span class="accent">WATCH</span></h2>

  <form class="optin-form">
    <div class="field">Name</div>
    <div class="field">Phone</div>
    <div class="field">Email</div>
    <div class="submit-btn">Submit</div>
  </form>

  <p class="fine-print">*we will send an email and a text message with the<br>&nbsp;offer and instructions on how to redeem</p>
</main>
</body>
</html>
```